Graphic Design Template for Digital Marketing Strategy

I require a template designing for a digital marketing strategy template, this will be a downloadable 2 page pdf.

One side will have a diagram showcasing all relevant DM strategies and how businesses should implement them, the following page will have a table that helps in the planning process.

I will provide all the content, however I need it to look professional, more importantly I need it to be a usable document for a business that lacks DM knowledge, so it needs to have implementable steps!

I have attached a similar document, this is good, however it does not get across the steps needs to be taken.

Also attached our logo.

Any questions please ask.

Owen

```html
<!DOCTYPE html>
<html lang="en">
<head>
<meta charset="utf-8">
<title>Web Strategy – Planning Template</title>
<link href="https://fonts.googleapis.com/css2?family=Arimo:wght@400;700&family=Barlow:wght@500&family=Oswald:wght@700&family=Questrial&display=swap" rel="stylesheet">
<style>
:root{
  --red:#e3262c;
  --ink:#1d1d1b;
  --grey-box:#c9c9cb;
  --tick-green:#5db638;
  --tick-red:#d9262b;
  --tick-blue:#2a9fd8;
  --ring:#7ec242;
  --web-blue:#2aa7df;
  --social-brown:#bf632b;
  --table-grey:#d9d9db;
  --table-line:#9fa3a6;
  --table-label:#3b7fc4;
  --muted:#b8b8b8;
}
*{box-sizing:border-box;margin:0;padding:0}
html,body{width:1200px;height:836px;overflow:hidden;background:#fff}
.spread{position:relative;width:1200px;height:836px;background:#fff;font-family:"Questrial",sans-serif;color:var(--ink)}
.abs{position:absolute;line-height:1;white-space:nowrap}

.page-no{font-family:"Arimo",sans-serif;color:var(--red);font-size:22px}
.title{font-family:"Arimo",sans-serif;font-weight:700;color:var(--red);font-size:27px}
.subtitle{font-family:"Arimo",sans-serif;font-weight:700;color:var(--red);font-size:19px}

.engine-name{font-size:30px;color:#4a78d1}
.heading{font-size:25px}
.search-field{background:var(--grey-box)}

.badge{text-align:center}
.badge .mark{display:block;margin:0 auto 5px;width:30px;height:30px;border-radius:50%;background:#eef0f2;border:1px solid #cfd3d6}
.badge .sq{position:absolute;left:8px;top:2px;width:11px;height:11px;background:#cde6f4}
.badge b{font-family:"Arimo",sans-serif;font-size:13px;display:block;margin-bottom:1px}
.badge span{font-size:12px;color:#444}

.tick-list{position:absolute;list-style:none}
.tick-list li{position:relative;font-size:16px;line-height:1}
.tick-list li::before{content:"";position:absolute;left:-17px;top:-1px;width:7px;height:14px;border:solid var(--tick);border-width:0 4px 4px 0;transform:rotate(38deg)}
.backlinks{--tick:var(--tick-green);left:61px;top:202px}
.backlinks li{height:25.2px}
.outcome{--tick:var(--tick-red);left:416px}
.outcome.blue{--tick:var(--tick-blue)}

.outcome-head{font-family:"Oswald",sans-serif;font-weight:700;font-size:23px;transform:translateX(-50%)}

.hub{position:absolute;left:138px;top:218px}
.hub-label{color:#fff;font-size:27px}
.screen-art{position:absolute;background:linear-gradient(#dfe7ee,#9fb0bf);border-radius:2px}
.social-title{font-family:"Barlow",sans-serif;font-weight:500;color:#fff;font-size:26px}
.channel{font-size:12px;color:#fff}
.channel::before{content:"";display:inline-block;width:7px;height:7px;background:#fff;margin-right:3px}

.brand{left:40px;top:668px;text-align:center;width:150px}
.brand .dot{display:block;margin:0 auto 8px;width:64px;height:64px;border-radius:50%;background:var(--tick-blue)}
.brand span{display:block;font-size:15px;line-height:1.05;color:var(--ink)}

.meta{font-family:"Arimo",sans-serif;font-size:8px;color:var(--red)}
.meta i{display:inline-block;width:170px;border-bottom:1px solid #999;margin-left:2px}

.plan{position:absolute;left:598px;top:103px;width:503px;border-collapse:collapse;font-family:"Arimo",sans-serif;font-size:6px;color:#333}
.plan td{border-top:1px solid var(--table-line);vertical-align:top;padding:2px 3px;line-height:1.2}
.plan .lbl{width:33px;color:var(--table-label);font-size:6.5px;vertical-align:middle}
.plan .q{width:126px}
.plan .c{width:172px;border-left:1px solid var(--table-line)}
.plan tr.shade td{background:var(--table-grey)}
.plan b{font-weight:700;font-size:6.5px}
.plan small{font-size:5px}
.plan tr.gap td{border:none;height:6px;padding:0;background:#fff}
.plan tr.when td{border-top:2px solid var(--table-line);border-bottom:2px solid var(--table-line)}
.score{position:relative}
.score .tag{position:absolute;left:2px;top:36px;transform:rotate(-90deg);transform-origin:left top;color:var(--table-label);font-size:5px}
.score .rows{padding-left:12px}
.score .goal{position:absolute;top:15px;font-size:9px;color:var(--muted)}

.chart-art{position:absolute;left:650px;top:470px;width:393px;height:250px;border:1px solid #e4e4e4;background:linear-gradient(90deg,#fbe3ae 0%,#c8e8ee 35%,#f6b7ae 62%,#bfe3d9 100%)}
</style>
</head>
<body>
<div class="spread">

  <!-- Page 2 : strategy diagram -->
  <div class="abs page-no" style="left:34px;top:42px">2</div>
  <div class="abs engine-name" style="left:212px;top:43px">Searchly</div>
  <div class="abs title" style="left:379px;top:40px">Web Strategy</div>

  <div class="abs heading" style="left:98px;top:77px">Search</div>
  <div class="abs search-field" style="left:185px;top:76px;width:158px;height:26px"></div>

  <div class="abs heading" style="left:62px;top:125px">Back Links</div>
  <div class="abs badge" style="left:190px;top:117px;width:95px">
    <i class="sq"></i><i class="mark"></i><b>SEO</b><span>Organic Searches</span>
  </div>
  <div class="abs badge" style="left:298px;top:117px;width:95px">
    <i class="sq"></i><i class="mark"></i><b>SEM</b><span>Searchly Ads</span>
  </div>
  <div class="abs heading" style="left:430px;top:125px">Outcomes</div>

  <ul class="tick-list backlinks">
    <li>Blogs</li><li>News Websites</li><li>Guest Blog Posts</li><li>Testimonials</li>
    <li>Speaker Bios</li><li>Expert Articles</li><li>Industry Partners</li><li>Blog Directories</li>
    <li>News Releases</li><li>Affilates</li><li>Awards</li><li>Galleries</li>
    <li>Infographics</li><li>Events</li><li>Threadly</li>
  </ul>

  <svg class="hub" width="320" height="480" viewBox="0 0 320 480" aria-hidden="true">
    <circle cx="142" cy="322" r="133" fill="#fff" stroke="var(--ring)" stroke-width="9"/>
    <circle cx="142" cy="322" r="118" fill="var(--social-brown)"/>
    <circle cx="160" cy="100" r="93" fill="#fff" stroke="var(--ring)" stroke-width="9"/>
    <circle cx="160" cy="100" r="79" fill="var(--web-blue)"/>
  </svg>
  <div class="abs hub-label" style="left:247px;top:306px">website</div>
  <div class="screen-art" role="img" aria-label="Desktop computer showing a website" style="left:262px;top:340px;width:55px;height:50px"></div>

  <div class="abs channel" style="left:212px;top:468px">Vidora</div>
  <div class="abs channel" style="left:264px;top:468px">Chirpr</div>
  <div class="abs channel" style="left:316px;top:468px">Tuneloop</div>
  <div class="abs social-title" style="left:190px;top:512px">SOCIAL MEDIA &amp;</div>
  <div class="abs social-title" style="left:190px;top:547px">MARKETING</div>
  <div class="abs channel" style="left:258px;top:606px">Feedline</div>

  <div class="abs outcome-head" style="left:477px;top:188px">Purchase</div>
  <ul class="tick-list outcome" style="top:221px">
    <li style="height:17px">Buy</li><li style="height:17px">Donate</li><li>Renew</li>
  </ul>
  <div class="abs outcome-head" style="left:478px;top:290px">Enquire</div>
  <ul class="tick-list outcome" style="top:318px">
    <li style="height:21px">Contact Us</li><li style="height:21px">Questionnaire</li><li>Apply Now</li>
  </ul>
  <div class="abs outcome-head" style="left:478px;top:406px">Connect</div>
  <ul class="tick-list outcome blue" style="top:441px">
    <li style="height:23px">Follow on Chirpr</li><li style="height:24px">Subscribe to Emails</li><li style="height:24px">“Like” on Friendbook</li>
    <li style="height:21px">Subscribe to Blog</li><li>Connect to Proflink</li>
  </ul>
  <div class="abs outcome-head" style="left:486px;top:561px">Download</div>
  <ul class="tick-list outcome blue" style="top:595px">
    <li style="height:22px">Flagship Content</li><li style="height:20px">Prenium Content</li><li style="height:20px">Ebooks</li><li>Template</li>
  </ul>

  <div class="abs brand"><i class="dot"></i><span>CLOUDLINE</span><span>DIGITAL</span></div>

  <!-- Page 4 : planning template -->
  <div class="abs subtitle" style="left:579px;top:46px">Web Strategy Planning Template</div>
  <div class="abs page-no" style="left:1107px;top:45px">4</div>
  <div class="abs meta" style="left:910px;top:77px">COMPANY<i></i></div>
  <div class="abs meta" style="left:910px;top:88px">PRODUCT/SERVICE: <i style="width:132px"></i></div>

  <table class="plan">
    <tr class="shade" style="height:31px">
      <td class="lbl">WHO</td>
      <td class="q"><b>Buyer Persona</b><br><b>Description</b><br>Who is this person?</td>
      <td class="c">1:</td><td class="c">2:</td>
    </tr>
    <tr style="height:66px">
      <td class="lbl">WHAT</td>
      <td class="q"><b>Problems you solve for this buyer?</b><br><small>Why are they buying from you?</small><br><b>Actions you'd like them to take:</b><br>Purchase<br>Enquire<br>Connect<br>Download</td>
      <td class="c"></td><td class="c"></td>
    </tr>
    <tr class="shade" style="height:40px">
      <td class="lbl">WHY</td>
      <td class="q"><b>How are you remarkable?</b><br><br><b>Proof</b><br><small>Guarentees, testimonials, press etc</small></td>
      <td class="c"></td><td class="c"></td>
    </tr>
    <tr style="height:26px">
      <td class="lbl">WHERE</td>
      <td class="q"><b>Where are they?</b><br><small>Searchly, blogs, Friendbook, Chirpr etc</small><br><small>Who do they trust?</small></td>
      <td class="c"></td><td class="c"></td>
    </tr>
    <tr class="shade" style="height:106px">
      <td class="lbl">HOW</td>
      <td class="q"><b>Content is King (Strategy)</b><br><br>What will you publish?<br><br><br>Keywords bases tree into Searchly.<br><br><b>Marketing is Queen (Tactics)</b><br><br>Blog, Chirpr, Vidora, email, newsletter,<br>e books, Friendbook, podcasts etc</td>
      <td class="c"></td><td class="c"></td>
    </tr>
    <tr class="gap"><td colspan="4"></td></tr>
    <tr class="when" style="height:42px">
      <td class="lbl">WHEN</td>
      <td class="q" colspan="2"><b>Things to do this week:</b><br>&nbsp;&nbsp;&nbsp;&nbsp;&nbsp;&nbsp;&nbsp;&nbsp;&nbsp;… this month:<br>&nbsp;&nbsp;&nbsp;&nbsp;&nbsp;&nbsp;&nbsp;… this quarter:<br>&nbsp;&nbsp;&nbsp;&nbsp;&nbsp;&nbsp;&nbsp;&nbsp;&nbsp;&nbsp;&nbsp;… this year:</td>
      <td class="c score">
        <span class="tag">SCORECARD</span>
        <div class="rows"><b>No. of Purchases:</b><br><b>No. of Enquiries:</b><br><b>No. of Connections:</b><br><b>No. of Downloads:</b></div>
        <span class="goal" style="left:94px">GOAL</span>
        <span class="goal" style="left:135px">RESULT</span>
      </td>
    </tr>
  </table>

  <div class="chart-art" role="img" aria-label="Infographic comparing usage across laptop, desktop, monitor and phone"></div>

</div>
</body>
</html>
```